Skill Up Salary Up

Full Page
7.5 w x 10 h / 8 w x 10.75 h + .25" bleed
Full-Page Career Course Ad
Project Overview
• Goal: Create a visually attractive, modern, and uncluttered full-page magazine advertisement to list available career courses.
• Tone: Creative, professional, and attention-grabbing to prevent the reader from turning the page. The final design must prioritize readability.

Content Requirements
1. Header/Headline: Must be the primary focus. And grab peoples attention
2. Course Listing: A clear, well-organized list of the career courses.
________________________________________
Design & Aesthetic Directives
1. Layout & Readability (Crucial)
• The final ad must not look crowded or busy.
• Prioritize white space to make the text "breathe" and ensure the course list is easy to scan and read.
• Use a modern, clean, and professional typeface (font choice is critical for the aesthetic).
2. Visual Style
• Aim for a creative, modern, and fresh look. Avoid outdated or generic stock imagery/layouts.
3. Imagery/Graphic Element (Artist's Choice)
You have creative freedom regarding the main graphic element.
• Option A (Photography): Use a photo of a white male American with a collared shirt. The imagery should convey success, focus, or professional development.
• Option B (Vector/Illustration): Use a modern vector graphic, illustration, or abstract design. This could be used to symbolize growth, connection, or a career path.
The choice of graphic element is yours, but it must support the overall modern and uncrowded aesthetic.

Requirements
Must have
• Partial listing .. is part of the Vocational Horizon Course

```html
<!DOCTYPE html>
<html lang="en">
<head>
<meta charset="utf-8">
<title>Skill Up, Salary Up – Career Courses</title>
<link href="https://fonts.googleapis.com/css2?family=Barlow+Condensed:wght@700&family=Figtree:wght@400;600;700;800&display=swap" rel="stylesheet">
<style>
:root{
  --blue:#0a9ad8;
  --navy:#243580;
  --orange:#eba024;
  --pale:#eaf6fc;
  --ink:#1f1f24;
  --grey-text:#333;
  --stage:#a9a9a9;
  --white:#fff;
}
*{box-sizing:border-box;margin:0;padding:0}
html,body{width:1200px;height:1117px;overflow:hidden;background:var(--stage)}
body{position:relative;font-family:"Figtree",sans-serif;color:var(--ink)}
.ad{position:absolute;left:194px;top:21px;width:1160px;height:1536px;transform:scale(.7);transform-origin:0 0;background:var(--pale);overflow:hidden;box-shadow:0 20px 50px rgba(0,0,0,.35)}
.hero-band{position:absolute;left:0;top:0;width:1160px;height:628px;background:var(--blue)}
.hero-art{position:absolute;left:0;top:0}
.headline{position:absolute;left:90px;top:58px;font-family:"Barlow Condensed",sans-serif;font-weight:700;font-size:86px;line-height:76px;color:var(--white);text-transform:uppercase;letter-spacing:.5px}
.headline-rule{position:absolute;left:90px;top:379px;width:458px;height:3px;background:var(--white)}
.tagline{position:absolute;left:93px;top:408px;font-size:29px;font-weight:700;color:var(--white);letter-spacing:.2px}
.card{position:absolute;background:var(--white);border-radius:14px;box-shadow:0 4px 10px rgba(0,0,0,.18);padding:8px 10px 0}
.card-title{background:var(--navy);color:var(--white);border-radius:6px;height:52px;display:flex;align-items:center;justify-content:center;font-size:28px;font-weight:700;text-transform:uppercase;letter-spacing:.3px}
.card-title.small{font-size:22px}
.card-body{padding:0 24px}
.ticks{list-style:none}
.ticks li{position:relative;padding-left:26px;font-size:20px;line-height:29.5px;color:var(--grey-text)}
.ticks li::before{content:"";position:absolute;left:0;top:9px;width:13px;height:13px;border-radius:50%;background:var(--navy)}
.ticks li::after{content:"";position:absolute;left:3.5px;top:12px;width:4px;height:6px;border:solid var(--white);border-width:0 2px 2px 0;transform:rotate(45deg)}
.ticks.light li::before{background:var(--blue)}
.ticks.bold li{font-weight:700;color:var(--ink);line-height:27px}
.ticks.inline{display:flex;gap:16px}
.ticks.inline li{padding-left:20px}
.ticks.inline li::before{left:0}
.ticks.inline li::after{left:3.5px}
.lead-blue{color:var(--blue);font-weight:700;font-size:20px}
.outline-box{border:2px solid var(--orange);border-radius:4px;text-align:center;color:var(--navy);font-weight:700}
.orange-bar{background:var(--orange);color:var(--white);border-radius:4px;text-align:center;font-weight:800;font-size:28px;height:42px;line-height:42px;text-transform:uppercase}
.schedule{text-align:center;font-size:20px;font-weight:800;color:var(--navy)}
.schedule span{color:var(--blue)}
.rank{color:var(--blue);font-weight:800;font-size:28px;line-height:30px}
.source{color:var(--orange);font-weight:700;font-size:20px}
.two-col{display:grid;grid-template-columns:156px 1fr}
.footer{position:absolute;left:0;top:1425px;width:1160px;height:111px;background:var(--navy);display:flex;align-items:center;justify-content:center;gap:26px;color:var(--white);font-size:35px;font-weight:800}
.footer .item{display:flex;align-items:center;gap:8px}
.footer .sep{width:2px;height:38px;background:var(--white)}
</style>
</head>
<body>
<main class="ad">
  <div class="hero-band"></div>
  <svg class="hero-art" width="1160" height="381" viewBox="0 0 1160 381">
    <defs>
      <linearGradient id="photoTone" x1="0" y1="0" x2="1" y2="1">
        <stop offset="0" stop-color="#4c5f6e"/>
        <stop offset=".5" stop-color="#2c4560"/>
        <stop offset="1" stop-color="#8a7a66"/>
      </linearGradient>
    </defs>
    <polygon points="495,0 540,0 630,253 575,381 540,381 600,253" fill="var(--orange)"/>
    <polygon points="540,0 1160,0 1160,381 575,381 630,253" fill="url(#photoTone)" role="img" aria-label="Photo of a smiling professional in a collared shirt working on a laptop in a modern office"/>
  </svg>
  <h1 class="headline">Skill Up,<br>Salary Up<br>Upcoming NVA<br>Courses</h1>
  <div class="headline-rule"></div>
  <p class="tagline">MEN &amp; WOMEN • IN-PERSON &amp; REMOTE • PARTIAL SCHOLORASHIPS</p>

  <section class="card" style="left:81px;top:463px;width:483px;height:520px">
    <h2 class="card-title">Vocational Horizon</h2>
    <div class="card-body" style="padding-top:14px">
      <p class="lead-blue">Business Skills &amp; Knowledge to:</p>
      <ul class="ticks light bold"><li>Impress your interviewer</li><li>Maxi mize Income</li></ul>
      <div class="outline-box" style="margin-top:16px;height:40px;line-height:36px;font-size:23px">Start / Run Your Business</div>
      <p class="schedule" style="margin-top:14px">4-5 MONTHS | <span>NOV 2025</span></p>
      <div class="orange-bar" style="margin-top:14px">Partial Listing</div>
      <div class="two-col" style="margin-top:6px">
        <ul class="ticks"><li>Computers</li><li>Marketing</li><li>Sales</li><li>Finance</li><li>Business Strategy</li></ul>
        <ul class="ticks"><li>Healthcare</li><li>Communication</li><li>LedgerPro</li><li>Investments</li><li>Real Estate</li><li>Accounting</li></ul>
      </div>
    </div>
  </section>

  <section class="card" style="left:601px;top:463px;width:483px;height:292px">
    <h2 class="card-title">Bookkeeping LedgerPro</h2>
    <div class="card-body" style="padding-top:12px">
      <p style="font-size:24px;font-weight:700;line-height:26px">Train for a quality job</p>
      <p style="font-size:24px;font-weight:700;line-height:26px;color:var(--blue)">Manage your own books</p>
      <ul class="ticks" style="margin-top:12px"><li>Finance Management</li><li>Customer &amp; Vendor Mgmt.</li><li>Advanced Tools</li></ul>
      <p class="schedule" style="margin-top:14px">5 WEEKS | <span>NOW 2025</span></p>
    </div>
  </section>

  <section class="card" style="left:601px;top:775px;width:483px;height:293px">
    <h2 class="card-title small">IT Desktop &amp; Networking Support</h2>
    <div class="card-body" style="padding-top:12px">
      <p class="rank">#2 Best Tech Job</p>
      <p class="source">National Career Review 2025</p>
      <div class="orange-bar" style="margin:10px -2px 0 -4px">Masters It:</div>
      <ul class="ticks inline" style="margin:10px -20px 0 -18px"><li>Desktop OS</li><li>Servers</li><li>Networks</li><li>Cloud</li></ul>
      <p class="schedule" style="margin-top:14px">7 MONTHS | <span>NOV 2025</span></p>
    </div>
  </section>

  <section class="card" style="left:81px;top:1025px;width:483px;height:365px">
    <h2 class="card-title">Software, Web &amp; Apps</h2>
    <div class="card-body" style="padding:12px 28px 0 10px">
      <p class="rank">#2 Best Tech Job</p>
      <p class="source">National Career Review 2025</p>
      <div class="orange-bar" style="margin:18px 0 0 5px;text-align:left;padding-left:30px">Job Prerequisite</div>
      <ul class="ticks" style="margin-top:6px"><li>Computer Programmer</li><li>Software Developer/Mobile</li><li>Engineer Developer (Apps</li></ul>
      <p class="schedule" style="margin-top:24px"><span>NOV 2025</span></p>
    </div>
  </section>

  <section class="card" style="left:601px;top:1090px;width:483px;height:300px">
    <h2 class="card-title">Office Suite- Computers</h2>
    <div class="card-body" style="padding-top:14px">
      <p class="source" style="font-weight:800">THE NEW JOB PREREQUISITE</p>
      <div style="display:grid;grid-template-columns:104px 1fr;margin:4px 0 0 10px">
        <ul class="ticks"><li>Sheets</li><li>Docs</li></ul>
        <ul class="ticks"><li>Email</li><li>Slides</li></ul>
      </div>
      <div class="outline-box" style="margin:12px 10px 0;height:40px;line-height:36px;font-size:18px">Computer lab available to practice</div>
      <p class="schedule" style="margin-top:28px"><span>NOV 2025</span></p>
    </div>
  </section>

  <footer class="footer">
    <span class="item"><svg width="24" height="24" viewBox="0 0 24 24"><circle cx="12" cy="12" r="11" fill="var(--blue)"/><circle cx="12" cy="12" r="5" fill="none" stroke="var(--navy)" stroke-width="2"/></svg>info@email.com</span>
    <span class="sep"></span>
    <span class="item"><svg width="24" height="24" viewBox="0 0 24 24"><circle cx="12" cy="12" r="11" fill="var(--blue)"/><rect x="6" y="8" width="12" height="8" fill="none" stroke="var(--navy)" stroke-width="1.6"/><path d="M6 8l6 5 6-5" fill="none" stroke="var(--navy)" stroke-width="1.6"/></svg>www.website.com</span>
    <span class="sep"></span>
    <span class="item"><svg width="20" height="28" viewBox="0 0 20 28"><path d="M5 2c2 0 3 5 3 6s-3 2-3 3c0 3 3 8 5 9 1 0 2-3 3-3s5 2 5 4-3 5-6 4C6 23 1 13 1 7 1 4 3 2 5 2z" fill="var(--blue)"/></svg>123-456-7890</span>
  </footer>
</main>
</body>
</html>
```